Re-branding for Structural Engineering firm

We need new business cards as part of our current re-branding. We have a new logo (attached), so the card design should incorporate this color scheme. We are a structural engineering firm providing structural building design and seismic consulting services. The final design should communicate professionalism and stability, with a modern look and feel.

```html
<!DOCTYPE html>
<html lang="en">
<head>
<meta charset="UTF-8">
<title>Oskerlin Structural Engineering – Business Card</title>
<link href="https://fonts.googleapis.com/css2?family=Crimson+Text:ital,wght@0,400;1,400&display=swap" rel="stylesheet">
<style>
  :root {
    --brand-blue: #2980ff;
    --accent-cyan: #4dd8ff;
    --paper: #ffffff;
    --plan-grey: #e9eaea;
    --ink-light: #ffffff;
  }
  html, body {
    margin: 0;
    padding: 0;
    width: 1200px;
    height: 686px;
    overflow: hidden;
    background: var(--paper);
  }
  .card {
    position: relative;
    width: 1200px;
    height: 686px;
    overflow: hidden;
    background: var(--paper);
    font-family: "Crimson Text", Georgia, serif;
  }
  .plan-backdrop {
    position: absolute;
    left: 0;
    top: 0;
    width: 700px;
    height: 686px;
    background: linear-gradient(135deg, #f4f5f5 0%, var(--paper) 45%, var(--plan-grey) 100%);
  }
  .geometry {
    position: absolute;
    inset: 0;
    width: 1200px;
    height: 686px;
  }
  .brand {
    position: absolute;
    left: 116px;
    top: 205px;
    width: 238px;
    display: flex;
    flex-direction: column;
    align-items: center;
    color: var(--brand-blue);
    text-align: center;
  }
  .brand-square {
    width: 160px;
    height: 160px;
    background: var(--brand-blue);
    margin-bottom: 16px;
  }
  .brand-name {
    font-size: 46px;
    line-height: 1;
    font-weight: 400;
  }
  .brand-tagline {
    font-size: 24px;
    line-height: 1.1;
    font-weight: 400;
    margin-top: 6px;
    white-space: nowrap;
  }
  .contact {
    position: absolute;
    left: 627px;
    top: 0;
    color: var(--ink-light);
  }
  .contact-name {
    position: absolute;
    left: 4px;
    top: 128px;
    margin: 0;
    font-size: 44px;
    line-height: 56px;
    font-style: italic;
    font-weight: 400;
    white-space: nowrap;
  }
  .contact-address,
  .contact-lines {
    position: absolute;
    left: 0;
    margin: 0;
    font-size: 35px;
    line-height: 48px;
    white-space: nowrap;
    font-style: normal;
  }
  .contact-address { top: 263px; }
  .contact-lines { top: 415px; }
  .contact-lines .label { margin-right: 12px; }
</style>
</head>
<body>
<div class="card">
  <div class="plan-backdrop" role="img" aria-label="Faint architectural floor plan drawing in light grey lines"></div>

  <svg class="geometry" viewBox="0 0 1500 857" preserveAspectRatio="none" aria-hidden="true">
    <polygon fill="var(--accent-cyan)" points="740,0 1500,0 1500,857 840,857 525,450 595,305"/>
    <polygon fill="var(--brand-blue)" points="860,0 1500,0 1500,857 822,857 590,320 670,155"/>
    <polygon fill="var(--brand-blue)" points="560,590 640,415 800,825"/>
    <line x1="866" y1="-4" x2="668" y2="158" stroke="var(--paper)" stroke-width="12"/>
    <line x1="590" y1="318" x2="830" y2="862" stroke="var(--paper)" stroke-width="10"/>
  </svg>

  <div class="brand">
    <div class="brand-square"></div>
    <div class="brand-name">Oskerlin</div>
    <div class="brand-tagline">Structural Engineering</div>
  </div>

  <div class="contact">
    <h1 class="contact-name">Mara Linden, S.E.</h1>
    <address class="contact-address">
      4150 Harbor Ridge Rd., Ste 210<br>
      Carlsbad, CA 92008
    </address>
    <p class="contact-lines">
      <span class="label">Phone:</span>555.214.3098<br>
      <span class="label">Cell:</span>555.387.6621<br>
      <span class="label">Email:</span>mara@oskerlinse.com
    </p>
  </div>
</div>
</body>
</html>
```